TrailMyPaces-fitness app follows the owner or client moves, let them monitor their weight & fitness

TrailMyPaces -fitness app, the avatar changes & evolve with the data logged in. the avatar resembles the client. the avatar weight looks like the client. When the client loses weight or gains weight, the avatar changes.
A brief is attached, check it out and get back to me with you're design.

Every week I will increase by 100€ instead.

Trailmypaces -fitness App Idea.
Two Business Logo.

March 2013 Ireland, the land of magic. Trailmypaces was born. Copy the client moves. With the avatar.
The app is about fitness, I have a vision and that you can be part of it.
Let's change the world together!
- the 1st page is about trailmypaces mission/founder/value of the company.
I will attach all information on Page(A)
after the intro, Terms and conditions poly/data policy ( the client has to agree and Sign before continuing. Then comes the page ParQ
the ParQ is a questionnaire asking the client to know more about them!
ParQ features the beginning: Create your personalized Avatar ( change clothes – if they choose no cloths, by default the avatar will have a pair of short- pant/hair/ eyes colour/ and select Body type: Ectomorph/ endomorph/ mesomorph or the client can select a mix body type.
Age select/ currant weight/ desired weight/ skin colour/ gender: male, female, Transgender, other.
Fitness goals: what the client desire how they are going to achieve it/ the measure they will take to achieve it or I don’t know option. The press continues / the app analyses all the data and create their personalise unique Avatar. That will look like the description they provided.
Page 2nd feature: they will see their full-body avatar.
Next, the client needs to continue completing more information.
Stress level select/ nutrition habits select/ and nutrition habit desired select/ injuries select/ allergies select/ history of any health complication question to answer/ Gp ( their Doctor name and number, to fill in/ and a person to contact in case of an emergency. Fill-in answer).
Page 3rd The Main Page. This results will depend on the answer of E-Wallet (5)
TrailMyPaces-fitness Pro APP, Will analyse all the data and the app will suggest the best fitness program, nutrition plan, meditation advice to help them with stress/ and sleep hours they need to recover from after exercise/ base on their body type, fitness goal, and current stress level.
Main page Features: Keep in mind; the avatar changes form constantly, all depend on the information the client put on the profile setting.
1- the Avatar
- the can look Happy
- or sad – the reason why! Can tell the client all the reason for being that way and the solutions to make it better.
- Angry- Reason why! Can tell the client all the reason for being that way and the solutions to make it better.
- if the client gain weight, it will show on the avatar body.
- When the client loses weight the avatar will tell the client with a notification and it shows o the avatar body.
2- fitness check the app call Brawnix and Gain Up fitness app, I like their page layout, it might show you what type of page I’m looking for and the quality that hoping or expecting.
- Muscle 3d full body when selecting a muscle it will show you the best exercises to work that particular muscle and weight recommendation. Check the app called
- Fitness Equipment to target each muscle and best suggestion for each muscle.
- Exercises all exercise available to get someone I top shape and the option to add more custom exercises. Liked exercise option/ search for exercises option/ reminder option.
- Nutrition Plans ( Vegan option/ paleo diet Option/ Keto diet/ build their own pers meal plan.
- Wellness Suggestions, tips raising your energy level
3- social Media
- Snapcove
- ChirpLine
- Boardly
- Friendnest
Feedback option
4- Music
- connect to Tunedrift.
- Connect to playlist Custom
- Connect to Melodex
5- E-wallet
- buy a 1to1 personal training session ( only for members living in the country as
the founder)
- Buy 1 sessions/ 45Minutes 45€
- Buy 1sessions / 30 Minutes 35€
- Buy 1 session / 60 Minutes 55€
App subscription ( 2 options)
- Buy one Month subscription 7.99€ app
- Buy one Year Subscription for 107.88€ Share it with 10 people for the best deal 49.99€ for 12 months.
6- share it
on any social platform on the list
7- Picture Gallery
- before Pic
- after pic
8 – Deals & Offers
link to affiliated with other organization( trailmypaces will put all fitness deals and offers on this page.
9 –Contacts
- Gps number and information
-- Friend or family to contact during an emergency
10- Testimonials
- Reviews
11- To-do List
- Calendar bookings
- fitness goal planner
12- Chat On The app community
- a page where all the app members can chat if they open the portal and agree to it.
13- Profile settings
- account settings
14-Progress Tracker
15 – Connect Fit Device
-- Progression CHART.
- Junk food / sweet tracker (obviously the client need to log in what they eat each time.
Base on what they eat the Avatar will take shape/ increase weight or lose weight / change mood/ the client will know when they are doing something wrong or right base on how the avatar mood.
I this idea is yours to be part of something different, this idea is will donate for young and family who need help and support.

WELCOME TO TrailMyPaces-fitness Private Studio
OUR MISSION
TrailMyPaces an Ireland based company whose mission is to help you
complete your journey stronger, faster with confidence.
ABOUT TRAILMYPACES
TrailMyPaces-fitness Was created from and inspire by the Irish strength and power to conquer any challenges, in 2013 after winning a boxing tournament in the national stadium. Driven by the desire to make a difference in the sports industry, I won that knight because my hunger for success was bigger than my opponents. TrailMyPaces-fitness Private Studio, I decided to teach and coach people, how to improve their fitness components with all the experience I have under my belt. My Mission is to inspire and be inspired by the new young talents in need for an opportunity.
TrailMyPaces-fitness Private Studio – Your energy is what keeps us moving and striving for a better and stronger united community. Fitness is the future & wellness is life.
I. OUR FOUNDER
Born and raised in the Caribbean, I started boxing when I was 19 years of age.
I started fighting to learn how to defend myself from bullying and protect my mother.
I started winning all my amateur fights, travelling around the world, the idea of travelling and the famous side of being a fighter kind started to like a little bit. My ambition didn’t stop there, it grew to aim for the stars and bigger plans.
I always dreamed of owning my own cloth brand and my own fitness gym. All over the Caribbean.
My peaceful Land (Dominican Rep, gave me the qualities to rise and achieve many goals. I believe- everything and anything is possible, once you have the right mindset and dedication to achieve it.
Trained by many of the best in coach in Ireland.
Now is time to share my knowledge.
OUR VALUES:
We value top quality Service and will ensure you have an amazing experience with TrailMyPaces Fitness. If not, write to us and we’ll make it right.
II. GIVING BACK:
To help and support those in need in our communities.
10% of our earning will be used to help and support people in need in the Dominican Republic, Haiti and all the Caribbean. We support our young athletes with big dreams. Seeing them succeed is the best gift the world can give us all.
Good Luck to all who will take this challenge. Remember this is only the start, the winner will gain an extra bonus for completing this work. And the chance to continue working with us.
III. You Can check the app call fitness Buddy or gain up a fitness app
these fitness features and setting is the style and standard I am looking for.

Target Market(s)

Fitness/ Nutrition & well Being

Contact Information for Business Card

Trailmypaces@quillbox.example
0871234096
www.trailmypacesfitness
The logo is on my brief.
On the card, I want trailMyPaces Fitness Pro.
I like an attractive colour like gold champagne on the main front side and on the back I want black and green to match the logo. sharp and professional style.

Font styles to use
Serif
Decorative
Script

Requirements
Must have
• Most have an option to create an avatar, to look like the client profile and weight/ hairstyle. This session is for the (App) https://vidhub.example/Qz81TrWpXaN
Ectomorph body type.
Endomorph body type.
mesomorph body type.
or a mix body type option.
base on the body type the client will be suggested by the trailmypaces the best plan for them.
Most have a challenges page: like squat challenge/ push-Ups challenge/ few fitness challenges to motivate the client.
Nice to have
• I would like to have every single muscle on the human body with all the exercises to work that particular muscle. like fitness buddy or gain Up fitness app
Must have a progression chart, to show the client his/her fitness progression on their: strength/ speed/ push-ups/ flexibility/ Cardio or their V02 Max.
also, Fitness test option; every month or even every the client wishes the can test their fitness.

I found an Idea on the net: https://vidhub.example/Qz81TrWpXaN
Thank you, a step closer to a better world.

```html
<!DOCTYPE html>
<html lang="en">
<head>
<meta charset="utf-8">
<title>TrailMyPaces Fitness – App Screens</title>
<link href="https://fonts.googleapis.com/css2?family=Roboto:ital,wght@0,300;0,400;0,500;0,700;1,400&display=swap" rel="stylesheet">
<style>
:root{
  --canvas:#e6e6e6;
  --teal:#40dcb4;
  --mint:#4fe0b0;
  --lime:#5ccf70;
  --forest-top:#3d7a6a;
  --forest-bottom:#0f2a22;
  --deep:#173d31;
  --white:#ffffff;
  --star:#f5a623;
  --skin-a:#c98d5c;
  --skin-b:#8a5633;
}
*{margin:0;padding:0;box-sizing:border-box}
html,body{width:1200px;height:438px;overflow:hidden;background:var(--canvas)}
body{position:relative;font-family:"Roboto",Arial,sans-serif;color:var(--white)}
.screen{position:absolute;top:19px;width:208px;height:388px;overflow:hidden;
  background:linear-gradient(180deg,var(--forest-top) 0%,#24574a 45%,var(--forest-bottom) 100%)}
.screen--intro{left:43px;background:linear-gradient(180deg,var(--teal) 0%,var(--lime) 62%)}
.screen--areas{left:265px}
.screen--gallery{left:497px}
.screen--reviews{left:721px}
.screen--challenges{left:952px}
.abs{position:absolute}
.center{left:0;right:0;text-align:center}
.title-light{font-weight:300;font-size:15px;letter-spacing:.2px}
.title-bold{font-weight:700;font-size:17px}
.figure{position:absolute;border-radius:45% 45% 30% 30%/30% 30% 20% 20%;
  background:linear-gradient(180deg,var(--skin-a),var(--skin-b))}
/* intro */
.intro-bottom{position:absolute;inset:0}
.brand{top:18px;font-size:14px;font-weight:500;letter-spacing:2px}
.intro-lose{top:62px;font-size:15px;font-weight:700}
.intro-build{top:83px;font-size:20px;font-weight:700}
.intro-days{top:308px;font-size:15px;font-weight:700}
.cta{position:absolute;left:45px;top:334px;width:114px;height:30px;border-radius:15px;
  background:linear-gradient(90deg,var(--teal),var(--lime));font-size:10px;font-weight:700;
  display:flex;align-items:center;justify-content:center;box-shadow:0 2px 6px rgba(0,0,0,.25)}
/* areas */
.pill{position:absolute;width:49px;height:26px;border-radius:13px;
  background:linear-gradient(90deg,var(--mint),var(--lime));font-size:10px;font-weight:700;
  display:flex;align-items:center;justify-content:center}
.connectors{position:absolute;inset:0}
/* gallery */
.person{top:80px;font-size:12px;font-weight:500}
.stat{top:101px;font-size:7.5px;line-height:10px}
.toggle{position:absolute;top:304px;width:72px;height:26px;border:1px solid var(--mint);border-radius:13px;
  font-size:11px;font-weight:500;display:flex;align-items:center;justify-content:center}
.toggle::before{content:"";position:absolute;top:-4px;left:50%;width:6px;height:6px;margin-left:-3px;
  border-left:1px solid var(--mint);border-top:1px solid var(--mint);background:#1a4438;transform:rotate(45deg)}
.dots{position:absolute;top:346px;left:87px;display:flex;gap:5px}
.dot{width:6px;height:6px;border-radius:50%;background:var(--white)}
.dot--empty{background:none;border:1px solid var(--white)}
/* reviews */
.review{position:absolute;left:18px;width:175px;height:79px;border:1px solid rgba(255,255,255,.85)}
.review--featured{height:87px;border:none;background:linear-gradient(180deg,#3fb795,#4fb36e)}
.avatar{position:absolute;left:12px;top:9px;width:22px;height:22px;border-radius:50%;
  background:linear-gradient(180deg,#e0b08a,#7a4a2d);border:1px solid var(--white)}
.reviewer{position:absolute;left:40px;top:9px;font-size:7px;font-weight:500}
.stars{position:absolute;left:40px;top:18px;font-size:7.5px;color:var(--star);letter-spacing:.5px}
.review-text{position:absolute;left:40px;top:30px;width:130px;font-size:5.3px;font-style:italic;line-height:9.2px}
.chevron{position:absolute;left:96px;top:358px}
/* challenges */
.goal-card{position:absolute;left:19px;top:99px;width:120px;height:69px;border-radius:12px 0 0 12px;
  background:linear-gradient(90deg,var(--mint),var(--lime));font-size:10px;font-weight:500;line-height:11px;padding:15px 0 0 18px}
.challenge{position:absolute;left:20px;width:104px;height:27px;border-radius:6px 0 0 6px;
  background:linear-gradient(90deg,var(--mint),var(--lime));font-size:10px;font-weight:500;
  display:flex;align-items:center;padding-left:17px}
</style>
</head>
<body>

<section class="screen screen--intro" aria-label="Intro screen">
  <svg class="intro-bottom" width="208" height="388" viewBox="0 0 208 388">
    <polygon points="0,242 104,302 208,242 208,388 0,388" fill="#1f4d3f"/>
    <polyline points="0,242 104,302 208,242" fill="none" stroke="#fff" stroke-width="3"/>
  </svg>
  <div class="abs center brand">TRAILMYPACES</div>
  <div class="abs center intro-lose">LOSE WEIGHT</div>
  <div class="abs center intro-build">BUILD MUSCLE</div>
  <div class="figure" style="left:28px;top:122px;width:66px;height:178px" role="img" aria-label="3D avatar of a man with a heavier build"></div>
  <div class="figure" style="left:118px;top:122px;width:60px;height:170px" role="img" aria-label="3D avatar of the same man, lean and muscular"></div>
  <div class="abs center intro-days">45 DAYS CHALLENGE</div>
  <div class="cta">GET START NOW</div>
</section>

<section class="screen screen--areas" aria-label="Exercise area screen">
  <div class="abs center title-light" style="top:18px">CHOOSE YOUR</div>
  <div class="abs center title-bold" style="top:36px">EXCERCISE AREA</div>
  <div class="figure" style="left:70px;top:100px;width:84px;height:285px" role="img" aria-label="3D muscular male avatar standing, front three-quarter view"></div>
  <svg class="connectors" width="208" height="388" viewBox="0 0 208 388" fill="none" stroke="#fff" stroke-width=".7">
    <polyline points="38,106 38,119 92,119"/>
    <polyline points="173,141 173,156 130,156"/>
    <polyline points="32,156 32,162 75,162"/>
    <polyline points="38,192 38,180 92,180"/>
    <polyline points="176,206 176,193 122,193"/>
    <polyline points="38,247 38,232 92,232"/>
    <polyline points="183,280 183,263 128,263"/>
    <polyline points="34,323 34,310 80,310"/>
  </svg>
  <div class="pill" style="left:14px;top:80px">TRAPS</div>
  <div class="pill" style="left:149px;top:115px">CHEST</div>
  <div class="pill" style="left:7px;top:130px">BICEPS</div>
  <div class="pill" style="left:14px;top:192px">LATS</div>
  <div class="pill" style="left:154px;top:206px">ABS</div>
  <div class="pill" style="left:14px;top:247px">GLUTE</div>
  <div class="pill" style="left:150px;top:280px">LEGS</div>
  <div class="pill" style="left:12px;top:323px">CALF</div>
</section>

<section class="screen screen--gallery" aria-label="Before and after gallery screen">
  <div class="abs center title-light" style="top:17px">OUR GALLERY</div>
  <div class="abs center title-bold" style="top:35px">BEFORE &amp; AFTER</div>
  <div class="abs center person">DARIO KEANE</div>
  <div class="abs center stat">LOSE WEIGHT<br>20 KG IN 45 DAYS</div>
  <svg class="abs" style="left:0;top:0" width="208" height="388" viewBox="0 0 208 388">
    <circle cx="25" cy="215" r="76" fill="#1f5e4a"/>
    <circle cx="183" cy="215" r="76" fill="url(#afterGlow)"/>
    <defs><linearGradient id="afterGlow" x1="0" y1="0" x2="1" y2="1"><stop offset="0" stop-color="#40dcb4"/><stop offset="1" stop-color="#5ccf70"/></linearGradient></defs>
  </svg>
  <div class="figure" style="left:14px;top:124px;width:72px;height:166px" role="img" aria-label="3D avatar side view before weight loss"></div>
  <div class="figure" style="left:150px;top:128px;width:40px;height:162px" role="img" aria-label="3D avatar side view after weight loss"></div>
  <div class="toggle" style="left:12px">BEFORE</div>
  <div class="toggle" style="left:127px">AFTER</div>
  <div class="dots"><span class="dot dot--empty"></span><span class="dot"></span><span class="dot"></span><span class="dot"></span></div>
</section>

<section class="screen screen--reviews" aria-label="Reviews screen">
  <div class="abs center title-light" style="top:16px">REVIEWS</div>
  <div class="abs center title-bold" style="top:34px">WHAT PEOPLE SAYS</div>
  <article class="review review--featured" style="top:73px">
    <div class="avatar" role="img" aria-label="Reviewer profile photo"></div>
    <div class="reviewer">Dario Keane</div>
    <div class="stars">★★★★★</div>
    <p class="review-text">Aec hendrerit quis leo Pellentesque rutrum malesuada neque Nunc tempus felis vitae urna Vivamus porttitor neque at volutpat rutrum purus nisi eleifend libero a tempus</p>
  </article>
  <article class="review" style="top:172px">
    <div class="avatar" role="img" aria-label="Reviewer profile photo"></div>
    <div class="reviewer">Nessa Quill</div>
    <div class="stars">★★★★★</div>
    <p class="review-text">Aec hendrerit quis leo Pellentesque rutrum malesuada neque Nunc tempus felis vitae urna Vivamus porttitor neque at volutpat rutrum purus nisi eleifend libero a tempus</p>
  </article>
  <article class="review" style="top:264px">
    <div class="avatar" role="img" aria-label="Reviewer profile photo"></div>
    <div class="reviewer">Dario Keane</div>
    <div class="stars">★★★★★</div>
    <p class="review-text">Aec hendrerit quis leo Pellentesque rutrum malesuada neque Nunc tempus felis vitae urna Vivamus porttitor neque at volutpat rutrum purus nisi eleifend libero a tempus</p>
  </article>
  <svg class="chevron" width="16" height="10" viewBox="0 0 16 10"><polyline points="1,1 8,8 15,1" fill="none" stroke="#4fe0b0" stroke-width="2"/></svg>
</section>

<section class="screen screen--challenges" aria-label="Challenges screen">
  <div class="abs center title-light" style="top:19px">BUILD MUSCLE</div>
  <div class="abs center title-bold" style="top:37px">CHALLENGES</div>
  <div class="goal-card">100 TO 1000 IN<br>ONE WEEK OR<br>ONE MONTH<br>OR PLUS</div>
  <div class="challenge" style="top:176px">SQUATS</div>
  <div class="challenge" style="top:213px">PUSH-UPS</div>
  <div class="challenge" style="top:252px">CARDIO</div>
  <div class="figure" style="left:108px;top:61px;width:88px;height:293px" role="img" aria-label="3D muscular male avatar standing, side three-quarter view"></div>
</section>

</body>
</html>
```